Electrician Flyer

Hi, I will provide all information needed for the flyer, just needing a cool design for a double sided flyer. Happy for a designer to play around with pictures, text, headings, boarders. The flyer will be standard size (A5). I have also uploaded a example flyer which I quite liked as a rough guide. Thanks

Target Market(s)

Adults

Industry/Entity Type

Electrician

Requirements
Must have
• Hi, I have uploaded some documents showing information needed on each side of the flyer (1st side of flyer, 2nd side of flyer). i am wanting the flyer to stand out and look professional. please add some images and possible stick to the color schemes of my logo,
Nice to have
• I have a plug type image on my Van, I was hoping to include this somewhere on the flyer. I have attached an image of the van for reference. Maybe image of a light bulb or something to make it less text heavy.

```html
<!DOCTYPE html>
<html lang="en">
<head>
<meta charset="utf-8">
<title>Voltara Electrical – 2015 Specials</title>
<link href="https://fonts.googleapis.com/css2?family=Alegreya+SC:wght@800&family=Open+Sans:wght@400;700;800&display=swap" rel="stylesheet">
<style>
  :root {
    --navy: #0b3a8c;
    --blue: #1f6fd0;
    --sky: #3fa3e6;
    --green: #a6cf2c;
    --lime: #9acd32;
    --white: #ffffff;
    --text-blue: #1a3f8f;
  }
  * { margin: 0; padding: 0; box-sizing: border-box; }
  html, body { width: 846px; height: 1200px; overflow: hidden; background: var(--white); }
  .flyer {
    position: relative; width: 846px; height: 1200px; overflow: hidden;
    background: var(--white);
    font-family: "Open Sans", Arial, sans-serif; color: var(--text-blue);
  }
  .header-art { position: absolute; left: 0; top: 0; width: 846px; height: 340px; }
  .hero-photo {
    position: absolute; left: 0; top: 0; width: 470px; height: 280px;
    background: radial-gradient(ellipse at 35% 40%, #d8e6f5 0%, #7fb0e0 35%, rgba(31,111,208,0) 75%);
  }
  .brand { position: absolute; right: 56px; top: 46px; text-align: right; }
  .brand-name {
    font-weight: 800; font-size: 64px; letter-spacing: 3px; line-height: 1;
    color: var(--green);
  }
  .brand-tag {
    margin-top: 2px; font-size: 13px; letter-spacing: 5.2px; color: var(--white);
  }
  .season-title {
    position: absolute; right: 56px; top: 146px;
    font-weight: 700; font-size: 34px; color: var(--white);
  }
  .offer-heading {
    font-family: "Alegreya SC", Georgia, serif; font-weight: 800;
    font-size: 24px; line-height: 25px; color: var(--navy); letter-spacing: 1.5px;
  }
  .offer-price { font-size: 20.5px; line-height: 24px; }
  .offer-desc { font-size: 20.5px; line-height: 26px; margin-top: 22px; }
  .offer { position: absolute; }
  .offer-downlights { left: 58px; top: 332px; width: 500px; }
  .offer-rcd { left: 305px; top: 570px; width: 440px; }
  .offer-security { left: 58px; top: 795px; width: 740px; }
  .product-photo { position: absolute; border-radius: 8px; }
  .photo-downlight {
    left: 560px; top: 305px; width: 270px; height: 175px;
    background: radial-gradient(ellipse at 45% 55%, #f3f3f3 0%, #dcdcdc 55%, rgba(255,255,255,0) 80%);
  }
  .photo-rcd {
    left: 88px; top: 498px; width: 178px; height: 272px;
    background: linear-gradient(180deg, #f1f1f1, #dedede);
  }
  .photo-security {
    left: 455px; top: 690px; width: 345px; height: 180px;
    background: radial-gradient(ellipse at 50% 50%, #d6d6d6 0%, #ececec 55%, rgba(255,255,255,0) 80%);
  }
  .footer-art { position: absolute; left: 0; top: 950px; width: 846px; height: 250px; }
  .slogan {
    position: absolute; left: 376px; top: 984px; width: 460px; text-align: center;
    font-weight: 700; font-size: 27px; line-height: 32px; color: var(--lime);
  }
  .contact {
    position: absolute; left: 0; top: 1106px; width: 846px; text-align: center;
    font-size: 22px; line-height: 24px; color: var(--text-blue); font-style: normal;
  }
</style>
</head>
<body>
<main class="flyer">
  <svg class="header-art" viewBox="0 0 846 340" aria-hidden="true">
    <defs>
      <linearGradient id="headerSky" x1="0" y1="0" x2="1" y2="0.4">
        <stop offset="0" stop-color="#0b4fa8"/>
        <stop offset="0.6" stop-color="#2b8ee0"/>
        <stop offset="1" stop-color="#4fb0ec"/>
      </linearGradient>
    </defs>
    <rect width="846" height="340" fill="url(#headerSky)"/>
    <path d="M0 300 C 260 230, 560 200, 846 215 L846 340 L0 340 Z" fill="#0b3a8c"/>
    <path d="M0 318 C 270 250, 570 220, 846 232 L846 340 L0 340 Z" fill="#a6cf2c"/>
    <path d="M0 336 C 280 265, 580 236, 846 244 L846 340 L0 340 Z" fill="#ffffff"/>
  </svg>
  <div class="hero-photo" role="img" aria-label="Photo of a clenched fist gripping a bright lightning bolt"></div>

  <div class="brand">
    <div class="brand-name">VOLTARA</div>
    <div class="brand-tag">ELECTRICAL &amp; COMMUNICATIONS</div>
  </div>
  <div class="season-title">2015 SPECIALS</div>

  <section class="offer offer-downlights">
    <h2 class="offer-heading">Supplied &amp; Installed High Quality<br>LED Down Lights</h2>
    <p class="offer-price">Just $99 each Inc GST</p>
    <p class="offer-desc">Energy-Efficient LED lights that add ambiance &amp;<br>Brightness into the room</p>
  </section>
  <div class="product-photo photo-downlight" role="img" aria-label="Photo of a white recessed LED down light with heat sink"></div>

  <div class="product-photo photo-rcd" role="img" aria-label="Photo of a white two-pole RCD safety switch"></div>
  <section class="offer offer-rcd">
    <h2 class="offer-heading">RCD'S Supplied and Installed</h2>
    <p class="offer-price">for $200 each inc GST</p>
    <p class="offer-desc">Safety Switches can Save your life,<br>please contact us for more information.</p>
  </section>

  <div class="product-photo photo-security" role="img" aria-label="Photo of a twin flood security light with motion sensor"></div>
  <section class="offer offer-security">
    <h2 class="offer-heading">Security Light Supplied<br>and Installed</h2>
    <p class="offer-price">for $160 inc GST</p>
    <p class="offer-desc">Compact Security Twin Flood Light In is a high quality and professional<br>floodlight which is designed to provide high illumination.</p>
  </section>

  <svg class="footer-art" viewBox="0 0 846 250" aria-hidden="true">
    <defs>
      <linearGradient id="footerGrey" x1="0" y1="0" x2="0" y2="1">
        <stop offset="0" stop-color="#ffffff"/>
        <stop offset="0.45" stop-color="#e2e2e2"/>
        <stop offset="1" stop-color="#bdbdbd"/>
      </linearGradient>
    </defs>
    <path d="M0 30 C 200 42, 420 55, 846 62 L846 250 L0 250 Z" fill="url(#footerGrey)"/>
    <path d="M0 10 C 150 22, 300 40, 470 56 C 300 50, 150 42, 0 36 Z" fill="#0b3a8c"/>
    <path d="M0 36 C 150 42, 300 50, 470 56 C 300 54, 150 48, 0 43 Z" fill="#a6cf2c"/>
    <path d="M0 146 C 300 138, 600 122, 846 104 L846 112 C 600 130, 300 145, 0 152 Z" fill="#a6cf2c"/>
    <path d="M0 152 C 300 145, 600 130, 846 112 L846 146 C 600 150, 300 154, 0 155 Z" fill="#0b3a8c"/>
  </svg>
  <p class="slogan">YOUR RELIABLE &amp;<br>AFFORDABLE ELECTRICIANS</p>
  <address class="contact">
    0400 123 456 | www.voltara.com.au | info@voltara.com.au<br>
    PO BOX 512 ASHVALE<br>
    EC 20481 | ACN: 12 345 678 901
  </address>
</main>
</body>
</html>
```